Therapy Services & Training

I provide counseling/therapy to individuals and families. I also travel the country and provide training at conferences.
I would like to see a card which takes my company name and design a logo using the letters "MCAC".
Target Market(s)
Therapists, non-profit organizations, clients looking for therapy
Industry/Entity Type
Training
Contact Information for Business Card
Meridel Clinical Advising & Coaching LLC
Danelle Brooks, M.S.W., LCSW
Clinical Therapist & Trainer
Providing clinical therapy services to individuals, families, couples & children. We also provide life coaching and crisis training.
helpdeskdanelle@mailbrook.example
www.meridelclinicaladvising.example
(555) 214-0397
Fernbrook, WD 01234
(BACK SIDE OF CARD)
We are certified by the Baseline Ongoing Lawyer Instruction (BOLI) Panel of the Statewide High Tribunal to provide Continuing Legal Education (CLE) credits to Westland attorneys. Call about what courses we offer! (555) 214-0397

```html
<!DOCTYPE html>
<html lang="en">
<head>
<meta charset="utf-8">
<title>Meridel Clinical Advising &amp; Coaching – Business Card</title>
<link rel="stylesheet" href="https://fonts.googleapis.com/css2?family=Lato:wght@400;700;900&display=swap">
<style>
  :root {
    --stage: #d9d9d9;
    --card-dark: #353535;
    --card-light: #ffffff;
    --ink-white: #ffffff;
    --ink-dark: #2b2b2b;
    --accent-blue: #7cc0ea;
    --accent-pink: #c64f9c;
    --accent-green: #5fc16b;
  }
  * { box-sizing: border-box; margin: 0; padding: 0; }
  html, body { width: 1200px; height: 800px; overflow: hidden; }
  body {
    background: var(--stage);
    font-family: "Lato", Arial, sans-serif;
    position: relative;
  }
  .card {
    position: absolute;
    box-shadow: 0 6px 18px rgba(0,0,0,0.25);
  }
  /* Front */
  .card-front {
    left: 105px; top: 135px;
    width: 330px; height: 555px;
    background: var(--card-dark);
    color: var(--ink-white);
    text-align: center;
    padding-top: 120px;
  }
  .brand-mark {
    display: flex; align-items: center; justify-content: center; gap: 12px;
    margin-bottom: 12px;
  }
  .brand-dot {
    width: 30px; height: 30px; border-radius: 50%;
    background: var(--accent-blue);
  }
  .brand-name {
    font-weight: 700; font-size: 46px; letter-spacing: 1px;
    color: var(--ink-white); line-height: 1;
  }
  .company-name {
    color: var(--accent-blue); font-size: 16.5px; text-transform: uppercase;
    line-height: 1.2; letter-spacing: 0.6px; margin-bottom: 26px;
  }
  .person-name {
    color: var(--accent-pink); font-size: 20px; text-transform: uppercase;
    letter-spacing: 0.8px; line-height: 1.1;
  }
  .person-role { font-size: 16px; line-height: 1.25; letter-spacing: 0.3px; margin-bottom: 26px; }
  .contact { font-size: 15.5px; line-height: 1.3; letter-spacing: 0.3px; margin-bottom: 26px; }
  .tagline { color: var(--accent-blue); font-size: 16px; line-height: 1.3; letter-spacing: 0.3px; }
  /* Back */
  .card-back {
    left: 570px; top: 205px;
    width: 560px; height: 360px;
    background: var(--card-light);
    color: var(--ink-dark);
    padding: 30px 36px;
  }
  .card-back .brand-mark { justify-content: flex-end; margin-bottom: 16px; padding-right: 20px; }
  .card-back .brand-dot { width: 60px; height: 60px; }
  .card-back .brand-name { color: var(--accent-blue); font-size: 60px; }
  .certification { font-size: 19px; line-height: 1.3; margin-bottom: 12px; }
  .hl-green { color: var(--accent-green); }
  .hl-pink { color: var(--accent-pink); }
  .call-out { font-size: 19px; line-height: 1.3; }
  .back-phone { color: var(--accent-blue); font-size: 28px; line-height: 1.2; }
</style>
</head>
<body>
  <section class="card card-front">
    <div class="brand-mark">
      <span class="brand-dot"></span>
      <span class="brand-name">MCAC</span>
    </div>
    <p class="company-name">Meridel Clinical<br>Advising &amp; Coaching LLC</p>
    <p class="person-name">Danelle Brooks</p>
    <p class="person-role">M.S.W., LCSW<br>Clinical Therapist &amp; Trainer</p>
    <p class="contact">(555) 214-0397<br>helpdeskdanelle@mailbrook.example<br>www.meridelclinicaladvising.example<br>Fernbrook, WD 01234</p>
    <p class="tagline">Providing clinical therapy services to<br>individuals, families, couples &amp; children.<br>We also provide life coaching and<br>crisis training.</p>
  </section>

  <section class="card card-back">
    <div class="brand-mark">
      <span class="brand-dot"></span>
      <span class="brand-name">MCAC</span>
    </div>
    <p class="certification">We are certified by the <span class="hl-green">Baseline Ongoing Lawyer Instruction (BOLI)</span> Panel of the Statewide High Tribunal to provide <span class="hl-pink">Continuing Legal Education (CLE)</span> credits to Westland attorneys.</p>
    <p class="call-out">Call about what courses we offer!</p>
    <p class="back-phone">(555) 214-0397</p>
  </section>
</body>
</html>
```